Business Cards for New Club President

I would like to get Business cards for the new president of our club. Our organization used Pixel Harbor last year to create a logo for an event and we love that logo. The new president really likes the logo and would like to use it for her personal logo. But since it was created for a specific event, it needs to be modified. She would like to keep the same basic design but add a strand of pearls winding through the image.

Contact Information for Business Card

Name of President, email, phone, location

Font styles to use
Serif

Colors
ec1f27
fff4ee

Requirements
Must have
• 1. A modified version of the image we previously purchased from Pixel Harbor. (see uploaded image); remove the name of the event and date..
2. A strand of pearls (or individual pearls) gracefully wrapping through the image.
3. The phrase "Maribel Alumnae" or "Maribel Alumnae Chapter" on the design
Nice to have
• Use the original design we purchased from Pixel Harbor
Should not have
• Should not have any other colors other than red, white or black.

```html
<!DOCTYPE html>
<html lang="en">
<head>
<meta charset="UTF-8">
<title>Maribel Alumnae Chapter – Business Card</title>
<link href="https://fonts.googleapis.com/css2?family=Poppins:wght@300;400;500&display=swap" rel="stylesheet">
<style>
  :root {
    --red: #c21f30;
    --white: #ffffff;
    --ink: #3a3a3a;
    --muted: #6b6b6b;
    --backdrop: #ece7e2;
  }
  * { margin: 0; padding: 0; box-sizing: border-box; }
  html, body {
    width: 1200px; height: 800px; overflow: hidden;
    background: var(--backdrop);
    font-family: "Poppins", sans-serif;
  }
  .stage { position: relative; width: 1200px; height: 800px; }

  .card {
    position: absolute;
    width: 540px; height: 309px;
    overflow: hidden;
    box-shadow: 0 6px 18px rgba(0,0,0,.18);
  }
  .card--front { left: 40px; top: 120px; background: var(--white); }
  .card--back  { left: 620px; top: 371px; background: var(--red); }

  /* Front */
  .front-wave { position: absolute; inset: 0; }
  .corner-tab {
    position: absolute; right: 0; top: 0;
    width: 44px; height: 10px; background: var(--red);
  }
  .mark {
    position: absolute; display: flex; align-items: center; gap: 8px;
    font-weight: 500; white-space: nowrap;
  }
  .mark__dot { width: 14px; height: 14px; border-radius: 50%; }
  .card--front .mark { left: 30px; top: 72px; color: var(--red); font-size: 19px; }
  .card--front .mark__dot { background: var(--red); }

  .identity { position: absolute; right: 30px; top: 44px; text-align: right; }
  .identity__name {
    color: var(--red); font-weight: 500; font-size: 24px;
    letter-spacing: .5px; line-height: 1.1;
  }
  .identity__role { color: var(--muted); font-size: 12px; font-weight: 400; margin-top: 2px; }

  .divider {
    position: absolute; left: 170px; right: 28px; top: 122px;
    height: 1px; background: var(--red);
  }

  .address {
    position: absolute; right: 30px; top: 134px; text-align: right;
    color: var(--ink); font-size: 12px; line-height: 1.45;
    font-style: normal; font-weight: 400;
  }

  .contacts {
    position: absolute; left: 170px; top: 134px;
    list-style: none; color: var(--ink); font-size: 13px; line-height: 1.5;
  }
  .contacts li { display: flex; align-items: center; gap: 7px; }
  .contacts svg { width: 10px; height: 10px; flex: none; }

  /* Back */
  .card--back .mark {
    left: 50%; top: 108px; transform: translateX(-50%);
    color: var(--white); font-size: 28px;
  }
  .card--back .mark__dot { background: var(--white); width: 20px; height: 20px; }
  .chapter-title {
    position: absolute; left: 0; right: 0; bottom: 62px; text-align: center;
    color: var(--white); font-size: 20px; font-weight: 400; letter-spacing: 1.5px;
  }
</style>
</head>
<body>
<main class="stage">

  <section class="card card--front" aria-label="Business card front">
    <svg class="front-wave" viewBox="0 0 540 309" width="540" height="309" aria-hidden="true">
      <path d="M120,309 C260,302 340,270 400,240 C450,215 495,204 540,198 L540,309 Z" fill="var(--red)"/>
      <path d="M150,309 C280,300 355,272 410,248 C460,226 500,214 540,209" fill="none" stroke="var(--white)" stroke-width="2"/>
      <path d="M80,307 C230,298 320,262 385,230 C435,205 485,192 540,186" fill="none" stroke="var(--red)" stroke-width="1.5"/>
    </svg>
    <div class="corner-tab"></div>

    <div class="mark"><span class="mark__dot"></span><span>Maribel Alumnae</span></div>

    <div class="identity">
      <div class="identity__name">DANIEL REYES</div>
      <div class="identity__role">Director</div>
    </div>

    <div class="divider"></div>

    <address class="address">412 Larkspur Lane<br>Fairview, OR 97024</address>

    <ul class="contacts">
      <li>
        <svg viewBox="0 0 10 10"><path d="M2,1 L4,1 L4.6,3 L3.4,4 C4,5.4 4.8,6.2 6,6.6 L7,5.4 L9,6 L9,8 C9,8.6 8.6,9 8,9 C4.5,8.8 1.2,5.5 1,2 C1,1.4 1.4,1 2,1 Z" fill="var(--red)"/></svg>
        041 555 20 37
      </li>
      <li>
        <svg viewBox="0 0 10 10"><rect x="0.8" y="2" width="8.4" height="6" fill="none" stroke="var(--red)" stroke-width="1.2"/><path d="M1,2.4 L5,5.4 L9,2.4" fill="none" stroke="var(--red)" stroke-width="1.2"/></svg>
        hello@ChapterDesk.org
      </li>
      <li>
        <svg viewBox="0 0 10 10"><circle cx="5" cy="5" r="4.2" fill="none" stroke="var(--red)" stroke-width="1.2"/><path d="M1,5 H9 M5,1 C3,3.5 3,6.5 5,9 M5,1 C7,3.5 7,6.5 5,9" fill="none" stroke="var(--red)" stroke-width="0.9"/></svg>
        www.ChapterDesk.org
      </li>
    </ul>
  </section>

  <section class="card card--back" aria-label="Business card back">
    <div class="mark"><span class="mark__dot"></span><span>Maribel Alumnae</span></div>
    <p class="chapter-title">MARIBEL ALUMNAE CHAPTER</p>
  </section>

</main>
</body>
</html>
```